Brisk Lantern Business Card

We need a business card design for an existing company (www.brisk-lantern.com). The business cards will be by Tavi in their Orra range (http://uk.tavi-print.example/products/orra/business-cards.html).

The card should be landscape, with the full company logo on the reverse side. I would like to have the card to portray a professional image (this is a high technology niche consultancy company). The card should be mostly white but aligned with our website (this is mostly dark colours). I can supply the logo files etc.

Details on the card should include the following:

Name (example: Gordon Pemberly)
Position (example: Principal Consultant)
Email Address (example: gordon@brisk-lantern.com)
Mobile Phone Number (example: +44 (0) 7519 804 372)
Website (example: www.brisk-lantern.com)
Twitter (example: @brisklanternco)
Facebook (example: www.facebook.com/brisklanternco)

I would like the text on the front of the card to be black. Thanks.

Requirements
Should not have
• The company address on the card.

```html
<!DOCTYPE html>
<html lang="en">
<head>
<meta charset="utf-8">
<title>Brisk Lantern Business Card</title>
<link rel="stylesheet" href="https://fonts.googleapis.com/css2?family=Open+Sans:wght@400;600;700&display=swap">
<style>
  :root {
    --backdrop: #d9d4cc;
    --card-dark: #222222;
    --band-grey: #464646;
    --rule-grey: #4c4c4c;
    --accent: #f07a1a;
    --text-light: #f2f2f2;
    --card-white: #ffffff;
    --text-grey: #4a4a4a;
  }
  * { box-sizing: border-box; margin: 0; padding: 0; }
  html, body {
    width: 1200px; height: 916px; overflow: hidden;
    background: var(--backdrop);
    font-family: "Open Sans", Arial, sans-serif;
  }
  .canvas { position: relative; width: 1200px; height: 916px; }

  .card {
    position: absolute; width: 580px; height: 330px;
    box-shadow: 0 4px 14px rgba(0,0,0,0.25);
  }

  /* Front */
  .card-front { left: 190px; top: 90px; background: var(--card-dark); color: var(--text-light); }
  .front-band { position: absolute; left: 0; top: 0; width: 100%; height: 14px; background: var(--band-grey); }
  .front-band-accent { position: absolute; left: 50%; top: 0; width: 160px; height: 14px; transform: translateX(-50%); background: var(--accent); }
  .front-mark {
    position: absolute; top: 44px; left: 0; width: 100%;
    display: flex; justify-content: center; align-items: center; gap: 10px;
    font-size: 15px; font-weight: 600; color: var(--accent); letter-spacing: 1px;
  }
  .front-mark-dot { width: 46px; height: 46px; border-radius: 50%; background: var(--accent); }
  .front-rule { position: absolute; left: 0; top: 136px; width: 100%; height: 2px; background: var(--rule-grey); }
  .person { position: absolute; top: 154px; left: 0; width: 100%; text-align: center; }
  .person-name { font-size: 20px; font-weight: 400; letter-spacing: 2px; text-transform: uppercase; }
  .person-role { font-size: 14px; color: var(--accent); margin-top: 2px; }
  .accent-rule { position: absolute; left: 50%; top: 226px; width: 160px; height: 3px; transform: translateX(-50%); background: var(--accent); }
  .contact {
    position: absolute; top: 240px; left: 0; width: 100%; text-align: center;
    font-size: 12.5px; line-height: 18px;
  }
  .contact-value { color: var(--accent); }
  .contact-gap { display: inline-block; width: 12px; }
  .contact-rule { position: absolute; left: 0; top: 290px; width: 100%; height: 2px; background: var(--rule-grey); }
  .contact-last { position: absolute; top: 300px; left: 0; width: 100%; text-align: center; font-size: 12.5px; }

  /* Reverse */
  .card-back { left: 330px; top: 490px; background: var(--card-white); }
  .brand { position: absolute; left: 56px; top: 122px; display: flex; align-items: center; gap: 18px; }
  .brand-dot { width: 86px; height: 86px; border-radius: 50%; background: var(--accent); flex: none; }
  .brand-name { font-size: 26px; font-weight: 700; color: var(--accent); text-transform: uppercase; letter-spacing: 0.5px; line-height: 1.1; white-space: nowrap; }
  .brand-tagline { font-size: 16px; color: var(--text-grey); letter-spacing: 0.8px; margin-top: 4px; white-space: nowrap; }
</style>
</head>
<body>
<main class="canvas">
  <section class="card card-front" aria-label="Card front">
    <div class="front-band"><div class="front-band-accent"></div></div>
    <div class="front-mark"><span class="front-mark-dot"></span><span>Brisk Lantern</span></div>
    <div class="front-rule"></div>
    <div class="person">
      <p class="person-name">Gordon Pemberly</p>
      <p class="person-role">Principal Consultant</p>
    </div>
    <div class="accent-rule"></div>
    <div class="contact">
      <p>Email : <span class="contact-value">gordon@brisk-lantern.com</span><span class="contact-gap"></span>Mobile : <span class="contact-value">+44 (0) 7519 804 372</span></p>
      <p>Website : <span class="contact-value">www.brisk-lantern.com</span><span class="contact-gap"></span>Twitter : <span class="contact-value">@brisklanternco</span></p>
    </div>
    <div class="contact-rule"></div>
    <p class="contact-last">Facebook : <span class="contact-value">www.facebook.com/brisklanternco</span></p>
  </section>

  <section class="card card-back" aria-label="Card reverse">
    <div class="brand">
      <span class="brand-dot"></span>
      <div>
        <p class="brand-name">Brisk Lantern Solutions</p>
        <p class="brand-tagline">Your Systems - Your Goals - Our Insight</p>
      </div>
    </div>
  </section>
</main>
</body>
</html>
```